Helicopter Medical Alert

I am looking for an app that quickly displays the coordinates of where the emergency is located. Once that is displayed then the ability for the caller to call 911 and the coordinates will still be displayed on the calling screen. Two examples I have researched are Zentrowick and Tollbyne. We don't have a call centre so the emergency number will solely be 911

Industry/Entity Type

Medical

```html
<!DOCTYPE html>
<html lang="en">
<head>
<meta charset="utf-8">
<title>Helicopter Medical Alert – Location Screen</title>
<link href="https://fonts.googleapis.com/css2?family=Open+Sans:wght@300;400;600;700&display=swap" rel="stylesheet">
<style>
  :root {
    --panel-top: #284a51;
    --panel-bottom: #1f3c43;
    --accent: #5ec5a6;
    --muted: #8ea3a5;
    --white: #ffffff;
    --status: #e6eeee;
    --button-border: #c9d4d4;
    --map-green: #b9d49a;
    --map-land: #ece9df;
    --map-sand: #e4dfcf;
  }
  * { box-sizing: border-box; margin: 0; padding: 0; }
  html, body { width: 739px; height: 1200px; overflow: hidden; }
  body {
    font-family: "Open Sans", Arial, sans-serif;
    background: var(--panel-bottom);
  }
  .app-screen {
    position: relative;
    width: 739px;
    height: 1200px;
    overflow: hidden;
  }
  .location-panel {
    position: relative;
    height: 790px;
    background: linear-gradient(180deg, var(--panel-top) 0%, var(--panel-bottom) 100%);
    color: var(--white);
  }
  .ridge-backdrop {
    position: absolute;
    left: 0; right: 0; bottom: 0;
    height: 220px;
    background: linear-gradient(180deg, rgba(47,80,88,0) 0%, rgba(47,80,88,0.55) 45%, rgba(31,60,67,0.9) 100%);
  }
  .status-bar {
    position: relative;
    display: flex;
    justify-content: space-between;
    align-items: center;
    height: 44px;
    padding: 0 18px;
    font-size: 24px;
    font-weight: 400;
    color: var(--status);
  }
  .status-left, .status-right { display: flex; align-items: center; gap: 8px; width: 230px; }
  .status-right { justify-content: flex-end; }
  .signal-dots { display: flex; gap: 3px; }
  .signal-dots span { width: 11px; height: 11px; border-radius: 50%; border: 1.5px solid var(--status); }
  .signal-dots span.on { background: var(--status); }
  .battery { width: 44px; height: 20px; border: 2px solid var(--status); border-radius: 4px; padding: 2px; position: relative; margin-right: 6px; }
  .battery::after { content: ""; position: absolute; right: -6px; top: 5px; width: 3px; height: 7px; background: var(--status); border-radius: 0 2px 2px 0; }
  .battery span { display: block; width: 100%; height: 100%; background: var(--status); border-radius: 1px; }

  .coordinates { position: relative; text-align: center; margin-top: 132px; }
  .coordinates-label { font-size: 22px; font-weight: 300; color: var(--accent); letter-spacing: 0.5px; }
  .coordinate { font-size: 58px; font-weight: 700; color: var(--accent); line-height: 1.25; letter-spacing: 0.5px; white-space: nowrap; }
  .coordinate-lat { margin-top: 12px; }
  .precision { margin-top: 38px; font-size: 17px; color: var(--muted); }

  .actions { position: relative; display: flex; flex-direction: column; align-items: center; gap: 32px; margin-top: 94px; }
  .action-button {
    display: flex; align-items: center;
    width: 366px; height: 76px;
    border: 3px solid var(--button-border);
    border-radius: 6px;
    color: var(--white);
    font-size: 27px; font-weight: 600;
    padding-left: 30px;
    gap: 34px;
    text-decoration: none;
  }
  .action-button svg { flex: none; }

  .area-map {
    height: 410px;
    background: linear-gradient(100deg, var(--map-land) 0%, var(--map-green) 30%, var(--map-green) 62%, var(--map-sand) 75%, var(--map-land) 100%);
  }
</style>
</head>
<body>
<main class="app-screen">
  <section class="location-panel">
    <div class="ridge-backdrop" role="img" aria-label="Faint misty mountain ridges behind the action buttons"></div>

    <header class="status-bar">
      <div class="status-left">
        <div class="signal-dots"><span class="on"></span><span class="on"></span><span class="on"></span><span></span><span></span></div>
        <span class="carrier">KESTREL</span>
        <svg width="24" height="18" viewBox="0 0 24 18" aria-hidden="true">
          <path d="M2 6a14 14 0 0 1 20 0M5.5 9.5a9 9 0 0 1 13 0M9 13a4 4 0 0 1 6 0" fill="none" stroke="#e6eeee" stroke-width="2.2" stroke-linecap="round"/>
          <circle cx="12" cy="16" r="1.6" fill="#e6eeee"/>
        </svg>
      </div>
      <span class="status-time">4:21 PM</span>
      <div class="status-right">
        <span class="battery-level">100%</span>
        <div class="battery"><span></span></div>
      </div>
    </header>

    <div class="coordinates">
      <p class="coordinates-label">YOU ARE HERE</p>
      <p class="coordinate coordinate-lat">40.4172871 N°</p>
      <p class="coordinate coordinate-lng">82.9071230023 W°</p>
      <p class="precision">(PRECISION 10 METERS)</p>
    </div>

    <nav class="actions">
      <a class="action-button call-button" href="tel:911">
        <svg width="32" height="32" viewBox="0 0 32 32" aria-hidden="true">
          <path d="M7 3l5 1 2 6-3 2.5a16 16 0 0 0 8.5 8.5L22 18l6 2 1 5-3 4C14 29 3 18 3 6z" fill="#ffffff"/>
          <path d="M18 9a6 6 0 0 1 5 5M18 4.5a10.5 10.5 0 0 1 9.5 9.5" fill="none" stroke="#ffffff" stroke-width="2.2" stroke-linecap="round"/>
        </svg>
        <span>CALL FOR HELP</span>
      </a>
      <a class="action-button aid-button" href="#first-aid">
        <svg width="28" height="26" viewBox="0 0 28 26" aria-hidden="true">
          <path d="M9 6V3h10v3" fill="none" stroke="#ffffff" stroke-width="2.4"/>
          <rect x="1" y="6" width="26" height="18" rx="3" fill="#ffffff"/>
          <path d="M14 10v10M9 15h10" stroke="#24434a" stroke-width="3.4"/>
        </svg>
        <span>FIRST AID TIPS</span>
      </a>
    </nav>
  </section>

  <section class="area-map" role="img" aria-label="Road map of the surrounding mountain region with a red pin marking the caller's position"></section>
</main>
</body>
</html>
```